Brixel Forge
Stationary for a S/W company
Brixel Forge -
Creative Brief
Use specific fonts
Dinesh Varma
Chief Operating Officer
14587 Harrow Court Brambleton, VA 20148
(800) 555 4bxf
(800) 555 2bxf
dinesh.varma@brixelforge.example
www.brixelforge.example
Front side: Dinesh Varma Chief Operating Officer t (703) 555 0147 dinesh.varma@brixelforge.example Back Side: www.brixelforge.example 14587 Harrow Court Brambleton, VA 20148 Toll free: t (800) 555 4bxf, f (800) 555 2bxf The key word is "CLEAN" and "Unique". If watermark, it should be really light. Normal edges. Pick the fonts and colors of your choice that will go with the logo. You can always try to keep all information on front but I want to keep the front of the business card as clean as possible with all "most used" information. The logo should be of focus. Same rule applies to letter head and envelopes. Also, need design for "thank you" cards and brochure. Good luck.
www.brixelforge.example 14587 Harrow Court, Brambleton, VA 20148 Toll free: t (800) 555 4bxf, f (800) 555 2bxf

```html
<!DOCTYPE html>
<html lang="en">
<head>
<meta charset="utf-8">
<title>Brixel Forge — Business Card</title>
<link href="https://fonts.googleapis.com/css2?family=Open+Sans:wght@300;400;600&display=swap" rel="stylesheet">
<style>
  :root {
    --stage: #0a0d4a;
    --stage-glow: #1a2790;
    --card-front: #ffffff;
    --card-back: #0f4784;
    --brand-navy: #1c3f7c;
    --accent: #2a9fd8;
    --accent-light: #3aaae6;
    --ink: #5a5a5a;
  }
  * { margin: 0; padding: 0; box-sizing: border-box; }
  html, body { width: 1200px; height: 1000px; overflow: hidden; }
  body {
    background: radial-gradient(ellipse at 50% 45%, var(--stage-glow) 0%, var(--stage) 70%);
    font-family: "Open Sans", Arial, sans-serif;
    position: relative;
  }
  .card {
    position: absolute;
    left: 249px;
    width: 662px;
    height: 378px;
  }
  .card--front { top: 76px; background: var(--card-front); }
  .card--back { top: 522px; background: var(--card-back); }

  .brand {
    position: absolute;
    right: 35px;
    top: 120px;
    display: flex;
    align-items: center;
    gap: 12px;
  }
  .brand__mark {
    width: 30px; height: 30px; border-radius: 50%;
    background: var(--accent);
  }
  .brand__name {
    font-size: 38px;
    font-weight: 300;
    color: var(--brand-navy);
    letter-spacing: 0.5px;
  }

  .person { position: absolute; left: 35px; top: 116px; }
  .person__name { font-size: 20px; font-weight: 600; color: var(--accent); line-height: 28px; }
  .person__title { font-size: 20px; font-weight: 300; color: var(--ink); line-height: 28px; }

  .address {
    position: absolute; left: 35px; top: 232px;
    font-size: 20px; font-weight: 300; color: var(--ink); line-height: 24px;
  }
  .address .label { color: var(--accent); font-weight: 600; display: inline-block; width: 30px; }
  .address .suffix { color: var(--accent); font-weight: 600; }

  .web {
    position: absolute; right: 35px; top: 304px; text-align: right;
    font-size: 20px; font-weight: 300; color: var(--ink); line-height: 24px;
  }

  .back-brand {
    position: absolute; inset: 0;
    display: flex; align-items: center; justify-content: center;
    font-size: 40px; font-weight: 300; color: var(--accent-light);
  }
</style>
</head>
<body>
  <section class="card card--front">
    <div class="brand">
      <span class="brand__mark"></span>
      <span class="brand__name">Brixel Forge</span>
    </div>
    <div class="person">
      <p class="person__name">Dinesh Varma</p>
      <p class="person__title">Chief Operating Officer</p>
    </div>
    <div class="address">
      <p>14587 Harrow Court</p>
      <p>Larkfield, VA 20392</p>
      <p><span class="label">tf:</span>800.555.4<span class="suffix">bxf</span></p>
      <p><span class="label">t:</span>703.555.0147</p>
      <p><span class="label">f:</span>800.555.2<span class="suffix">bxf</span></p>
    </div>
    <div class="web">
      <p>www.brixelforge.example</p>
      <p>dinesh.varma@brixelforge.example</p>
    </div>
  </section>

  <section class="card card--back">
    <div class="back-brand">Brixel Forge</div>
  </section>
</body>
</html>
```